Comet Raiders Movie Themed Coffee bag Label

We have a line of comet raiders themed roasted coffee. We want to have labels for these coffees which are Comet Raiders themed. The names of the coffees are Morlox, Brin, and Dunerover. I have attached a label similar to what we use today which also includes our logo. Attaching our logo also.

Target Market(s)

Coffee Lovers and Comet Raiders movie lovers

Industry/Entity Type

Coffee Shop

Font styles to use
Other font styles liked:
• News Gothic

Requirements
Must have
• our logo and web address. www.cedarloftroastingcompany.com, name of coffee, 14oz
Nice to have
• Comet Raiders like images, fonts, colors, etc

```html
<!DOCTYPE html>
<html lang="en">
<head>
<meta charset="utf-8">
<title>Cedar Loft Roasting Company – Morlox Medium Roast Label</title>
<link rel="stylesheet" href="https://fonts.googleapis.com/css2?family=News+Cycle:wght@400;700&family=Open+Sans:wght@400&family=Russo+One&display=swap">
<style>
  :root {
    --space-deep: #1c1630;
    --space-violet: #4a3560;
    --space-rose: #7a4a5c;
    --space-blue: #2c3a66;
    --band-dark: #353535;
    --band-edge: #e8762a;
    --badge-white: #ffffff;
    --brand-brown: #5a2e14;
    --gold-light: #fff1b0;
    --gold-mid: #f4c232;
    --gold-deep: #c98a14;
    --text-white: #ffffff;
    --net-yellow: #f2e23a;
  }
  html, body {
    margin: 0;
    padding: 0;
    width: 858px;
    height: 1200px;
    overflow: hidden;
    background: #ffffff;
  }
  .label {
    position: relative;
    width: 858px;
    height: 1200px;
    border-radius: 32px;
    overflow: hidden;
  }
  .galaxy-backdrop {
    position: absolute;
    inset: 0;
    background:
      radial-gradient(ellipse at 70% 20%, var(--space-rose) 0%, transparent 45%),
      radial-gradient(ellipse at 20% 85%, var(--space-blue) 0%, transparent 50%),
      radial-gradient(ellipse at 80% 90%, var(--space-rose) 0%, transparent 40%),
      linear-gradient(160deg, var(--space-violet), var(--space-deep) 55%, var(--space-violet));
  }
  .roast-band {
    position: absolute;
    left: 0;
    top: 382px;
    width: 858px;
    height: 442px;
    background: var(--band-dark);
  }
  .roast-band::before,
  .roast-band::after {
    content: "";
    position: absolute;
    left: 0;
    width: 100%;
    height: 3px;
    background: linear-gradient(90deg, var(--band-edge), #f6b23c 50%, var(--band-edge));
  }
  .roast-band::before { top: 20px; }
  .roast-band::after { bottom: 2px; }
  .brand-disc {
    position: absolute;
    left: 181px;
    top: 116px;
    width: 496px;
    height: 496px;
    border-radius: 50%;
    background: var(--badge-white);
  }
  .brand-name {
    position: absolute;
    left: 181px;
    top: 116px;
    width: 496px;
    height: 496px;
    display: flex;
    flex-direction: column;
    align-items: center;
    justify-content: center;
    font-family: "News Cycle", sans-serif;
    font-weight: 700;
    color: var(--brand-brown);
    text-align: center;
    line-height: 1;
  }
  .brand-name .brand-main { font-size: 84px; }
  .brand-name .brand-sub {
    font-size: 40px;
    letter-spacing: 1px;
    text-transform: uppercase;
    margin-top: 14px;
  }
  .coffee-name {
    position: absolute;
    left: 0;
    top: 634px;
    width: 858px;
    margin: 0;
    text-align: center;
    font-family: "Russo One", sans-serif;
    font-weight: 400;
    font-size: 134px;
    line-height: 1;
    letter-spacing: -4px;
    background: linear-gradient(90deg, var(--gold-deep), var(--gold-mid) 35%, var(--gold-light) 75%, var(--gold-mid));
    -webkit-background-clip: text;
    background-clip: text;
    color: transparent;
    -webkit-text-stroke: 2px var(--band-edge);
  }
  .roast-level {
    position: absolute;
    left: 0;
    top: 756px;
    width: 858px;
    text-align: center;
    font-family: "Russo One", sans-serif;
    font-size: 33px;
    line-height: 1;
    letter-spacing: -1px;
    color: var(--text-white);
  }
  .tagline {
    position: absolute;
    left: 0;
    top: 924px;
    width: 858px;
    margin: 0;
    text-align: center;
    font-family: "Russo One", sans-serif;
    font-size: 39px;
    line-height: 39px;
    letter-spacing: -1px;
    color: var(--text-white);
    text-transform: uppercase;
  }
  .web-address {
    position: absolute;
    left: 0;
    top: 1090px;
    width: 858px;
    text-align: center;
    font-family: "Open Sans", sans-serif;
    font-size: 31px;
    line-height: 1.2;
    color: var(--text-white);
  }
  .net-weight {
    position: absolute;
    left: 0;
    top: 1148px;
    width: 858px;
    text-align: center;
    font-family: "News Cycle", sans-serif;
    font-weight: 700;
    font-size: 26px;
    line-height: 1.2;
    color: var(--net-yellow);
  }
</style>
</head>
<body>
  <div class="label">
    <div class="galaxy-backdrop" role="img" aria-label="Swirling purple and rose galaxy nebula full of stars"></div>
    <div class="roast-band"></div>
    <div class="brand-disc"></div>
    <div class="brand-name">
      <span class="brand-main">Cedar Loft</span>
      <span class="brand-sub">Roasting Company</span>
    </div>
    <h1 class="coffee-name">MORLOX</h1>
    <div class="roast-level">MEDIUM ROAST</div>
    <p class="tagline">Freshly roasted coffee<br>that will take you<br>to a galaxy far far away</p>
    <div class="web-address">www.cedarloftroastingcompany.com</div>
    <div class="net-weight">NET WT 14oz</div>
  </div>
</body>
</html>
```